PLUMBING VAN LOGO/VINYL GRAPHIC CONTEST!

Our target audience is builders, contractors, designers, architects.

Upon discussion with some vinyl wrap companies we are now moving away from a full wrap and going for more simplistic lettering and logo design on the truck.
We are looking to apply vinyl graphics on top of a silver color Brannoc hauler 3400. (See attached picture for JUST CUT VINYL style design.

We would like to have our logo incorporated on to the sides of the truck (Must be shrunken down to fit the full logo - no cut off half images)

We would also like to have Custom homes, Additions, Renovations, as well as Commercial/Industrial incorporated onto the side of the van and also the back doors.

We would like to see variations of black and blue on top of the silver for a good color contrast. No light colours for the writing.

Hi Designers,

We are going to be changing the overall design stance of our project, we didn't find anything we particularly liked enough to use as a wrap for our trucks.

We would like to see some more simplistic ideas, and we have decided to keep the silver color of our trucks as a background. We will be going with vinyl graphics on top of the silver backdrop, instead of a full van wrap/color change.

With any new submissions, we would prefer to see our logo and our services listed on the truck, with different ideas for placement. Having a silver van color, we would prefer some darker bolder colors like black, blue, etc. and to avoid any light color schemes.

Important things to have on the design

Kestrow Plumbing Ltd
(logo)
(custom homes, additions, renovations)
(commercial/industrial)

Thank you to everybody who has/will submit designs.

• We are open to different fonts. We like the font in the logo but are open to other ideas.

• Kestrow Plumbing Ltd , Custom Homes, Additions, Renovations, Commercial/Residential
• Silver background on van, kestrow plumbing logo and kestrow plumbing ltd written on

```html
<!DOCTYPE html>
<html lang="en">
<head>
<meta charset="utf-8">
<title>Kestrow Plumbing – Van Side Vinyl</title>
<link href="https://fonts.googleapis.com/css2?family=Rubik:wght@700;800&family=Righteous&display=swap" rel="stylesheet">
<style>
  :root {
    --page: #ffffff;
    --silver: #b3b6ba;
    --silver-light: #d3d5d8;
    --silver-dark: #8a8d91;
    --trim: #4a4c50;
    --vinyl-black: #111214;
    --brand-blue: #1559b8;
    --glass: #2a2d32;
    --tire: #161616;
    --rim: #c9cbcd;
    --tail-red: #c8202a;
    --lamp: #e4e6e8;
  }
  html, body {
    margin: 0;
    padding: 0;
    width: 1200px;
    height: 797px;
    overflow: hidden;
    background: var(--page);
  }
  .van-side { display: block; width: 1200px; height: 797px; }
  .headline { font-family: "Rubik", sans-serif; font-weight: 800; }
  .tagline { font-family: "Righteous", sans-serif; }
  .wordmark { font-family: "Rubik", sans-serif; font-weight: 700; }
</style>
</head>
<body>
<svg class="van-side" viewBox="0 0 2000 1333" xmlns="http://www.w3.org/2000/svg">
  <defs>
    <linearGradient id="silver-paint" x1="0" y1="0" x2="0" y2="1">
      <stop offset="0" stop-color="var(--silver-light)"/>
      <stop offset="0.55" stop-color="var(--silver)"/>
      <stop offset="1" stop-color="var(--silver-dark)"/>
    </linearGradient>
  </defs>

  <ellipse class="ground-shadow" cx="1000" cy="940" rx="900" ry="40" fill="#000" opacity="0.12"/>

  <!-- van body, silver paint -->
  <path class="body" fill="url(#silver-paint)"
        d="M140 850 L135 770 Q140 700 170 680 Q230 650 330 625 L400 605 Q520 420 640 340 Q680 315 740 310 L1775 300 Q1815 302 1822 330 L1858 600 L1862 760 L1862 850 L1575 850 A108 108 0 0 0 1362 850 L455 850 A108 108 0 0 0 235 850 Z"/>

  <!-- panel seams -->
  <path class="panel-seam" d="M712 312 L712 875 M1105 304 L1105 875" stroke="var(--silver-dark)" stroke-width="3" fill="none"/>

  <!-- lower trim -->
  <path class="rocker" fill="var(--trim)" d="M455 850 L455 870 Q470 884 500 884 L1330 880 Q1355 878 1362 850 Z"/>
  <path class="rocker" fill="var(--trim)" d="M1575 850 L1862 850 L1862 800 L1810 800 L1810 850 Z"/>
  <path class="front-bumper" fill="var(--trim)" d="M135 770 L140 850 L235 850 Q240 790 290 765 L150 760 Z"/>

  <!-- side window -->
  <path class="glass" fill="var(--glass)"
        d="M450 615 L530 455 Q545 430 575 428 L668 425 Q680 427 676 440 L660 560 Z"/>
  <!-- mirror -->
  <rect class="mirror" x="412" y="540" width="28" height="72" rx="8" fill="var(--trim)"/>

  <!-- lamps -->
  <path class="headlight" fill="var(--lamp)" stroke="var(--trim)" stroke-width="3" d="M158 690 L245 672 L235 705 L165 722 Z"/>
  <rect class="tail-light" x="1815" y="600" width="42" height="150" rx="6" fill="var(--tail-red)"/>

  <!-- cut vinyl: upper swoosh -->
  <path class="vinyl-blue" fill="var(--brand-blue)"
        d="M915 306 L940 306 L790 548 L400 652 L245 678 L240 664 L385 634 L762 525 Z"/>
  <path class="vinyl-black" fill="var(--vinyl-black)"
        d="M880 320 L892 320 L745 515 L700 530 L698 522 L738 508 Z"/>

  <!-- cut vinyl: lower swoosh -->
  <path class="vinyl-blue" fill="var(--brand-blue)"
        d="M900 757 L1745 612 L1800 750 L1780 750 L1733 636 L960 758 Z"/>
  <path class="vinyl-black" fill="var(--vinyl-black)"
        d="M1040 760 L1720 658 L1782 748 L1766 748 L1712 674 L1062 762 Z"/>
  <path class="vinyl-blue" fill="var(--brand-blue)" d="M462 834 L640 818 L470 846 Z"/>

  <!-- wheels -->
  <g class="wheel">
    <circle cx="345" cy="885" r="98" fill="var(--tire)"/>
    <circle cx="345" cy="885" r="56" fill="var(--rim)"/>
    <circle cx="345" cy="885" r="22" fill="#555"/>
  </g>
  <g class="wheel">
    <circle cx="1468" cy="885" r="98" fill="var(--tire)"/>
    <circle cx="1468" cy="885" r="56" fill="var(--rim)"/>
    <circle cx="1468" cy="885" r="22" fill="#555"/>
  </g>

  <!-- services -->
  <text class="tagline services" x="870" y="468" font-size="34" fill="var(--brand-blue)"
        transform="rotate(-9 870 468)" textLength="650" lengthAdjust="spacingAndGlyphs">Custom Homes · Additions · Renovations</text>

  <!-- company name -->
  <text class="headline company-name" x="862" y="600" font-size="160" fill="var(--vinyl-black)"
        transform="rotate(-9 862 600)" textLength="670" lengthAdjust="spacingAndGlyphs">KESTROW</text>
  <text class="headline company-trade" x="982" y="650" font-size="92" fill="var(--brand-blue)"
        transform="rotate(-9 982 650)" textLength="445" lengthAdjust="spacingAndGlyphs">PLUMBING</text>

  <!-- phone -->
  <g class="phone-icon" transform="rotate(-9 870 722)">
    <circle cx="870" cy="722" r="34" fill="none" stroke="var(--brand-blue)" stroke-width="6"/>
    <path d="M858 705 q-8 6 -2 20 q8 16 22 18 l6 -8 l-9 -7 l-5 4 q-8 -5 -11 -13 l5 -4 l-4 -10 Z" fill="var(--brand-blue)"/>
  </g>
  <text class="headline phone-number" x="925" y="752" font-size="104" fill="var(--vinyl-black)"
        transform="rotate(-9 925 752)" textLength="595" lengthAdjust="spacingAndGlyphs">123-555-0142</text>

  <!-- sectors -->
  <text class="tagline sector" x="465" y="708" font-size="38" fill="var(--vinyl-black)"
        transform="rotate(-9 465 708)">Commercial</text>
  <text class="tagline sector" x="472" y="752" font-size="38" fill="var(--vinyl-black)"
        transform="rotate(-9 472 752)">Residential</text>
  <text class="headline ampersand" x="672" y="742" font-size="96" fill="var(--brand-blue)"
        transform="rotate(-9 672 742)">&amp;</text>

  <!-- company mark -->
  <g class="brand-badge">
    <circle cx="1640" cy="473" r="83" fill="var(--brand-blue)"/>
    <text class="wordmark" x="1640" y="481" font-size="24" fill="#ffffff" text-anchor="middle">KESTROW</text>
  </g>
</svg>
</body>
</html>
```